Lantern and Keystone Website

We are a private investigation that people turn to when they seek answers. We provide all types of investigation services as well as security and debt collection but mainly we specialise in digital forensic investigation. This site will be the first representation that potential clients see. We need a site that can work on all browsers so not too many animations. The theme we are going for is "Hollow" the TV show but keeping the law enforcement look. We want it to expand on the logo of our company that is strength and pride (refer to files attached). The logo and mission statement must stand out.
The relevant info is attached in .doc documents

Hi,

I have uploaded a slightly different version of the logo and I do prefer the new version and made a FEW but important updates and additions to the website info. Sorry for the inconvenience.

Hi, 

Sorry just one last thing can you please put the following on the website 'Lantern and Keystone is a South Australian owned business and we service all of Australia.' 

I have increased the budget.

Hi,

I've increased the budget slightly. I will continue to increase it as long as the quality of designs match it.

I have increased the budget. I will increase it more if I see some designs that warrant the increase.

I have extended the deadline by 3 days.

Hi,

Forget the brief and please take a look at this link and that is the type of design I want. I want people to look at it and think modern, professional, digital, forensic investigation. I have not seen anything that makes me think "wow" so please submit some new designs. I will increase the budget when I start to see designs that I like. 

regarding the last message, this is the link

https://www.brelvanoffice.example

Reason: Have not seen anything that stands out from the rest.

Reason: To let designers finish off their current concepts that they may be working on.

Target Market(s)

Average to corporate people seeking professionalism and a firm that can supply answers that traditional law enforcement agencies fail to provide

Industry/Entity Type

Security

Requirements
Must have
• A professional NRB, Coastal Ward Constabulary website look mixed with a theme from the TV show "Hollow" and the ability to download the business cards (refer to attached files)
Should not have
• cartoon images and anything relating to Percival Thorne

```html
<!DOCTYPE html>
<html lang="en">
<head>
<meta charset="utf-8">
<title>Lantern and Keystone</title>
<link href="https://fonts.googleapis.com/css2?family=Arimo:wght@400;700&family=Roboto+Condensed:wght@400;700&display=swap" rel="stylesheet">
<style>
:root{
  --cream:#efeadb;
  --cream-light:#f7f4ea;
  --ink:#2b2b2b;
  --text:#3a3a3a;
  --blue:#1d4f9c;
  --gold:#d9b35a;
  --gold-dark:#9c7a2a;
  --night:#0b0f14;
  --night-blue:#1b2a38;
  --muted:#b8bcc0;
  --link:#4f8ed6;
  --footer:#1c1c1c;
  --footer-text:#a9a9a9;
}
*{margin:0;padding:0;box-sizing:border-box}
html,body{width:1200px;height:1037px;overflow:hidden}
body{position:relative;background:var(--cream);font-family:"Arimo",Arial,sans-serif;color:var(--text)}

.intro{position:absolute;left:0;top:0;width:1200px;height:446px;
  background:radial-gradient(ellipse at 30% 40%,var(--cream-light) 0%,var(--cream) 60%,#e4dcc6 100%)}

.topbar{position:absolute;left:128px;top:0;width:943px;height:57px;
  background:linear-gradient(#2a2a2a,#0e0e0e);border-radius:0 0 4px 4px;
  box-shadow:0 3px 8px rgba(0,0,0,.35);font-family:"Roboto Condensed",Arial,sans-serif}
.topbar .mark{position:absolute;left:22px;top:8px;width:40px;height:40px;border-radius:50%;border:2px solid var(--gold-dark);background:#141414}
.nav{position:absolute;left:0;top:18px;list-style:none}
.nav li{position:absolute;top:0;white-space:nowrap;font-size:18px;color:#e6e6e6;letter-spacing:.2px}
.nav li.current{color:#fff;font-weight:700}
.call{position:absolute;left:733px;top:15px;display:flex;align-items:center;gap:8px;font-size:21px;color:#fff;white-space:nowrap}
.call b{color:var(--gold);font-weight:400}

.brand{position:absolute;left:175px;top:165px;width:300px;display:flex;align-items:center;gap:14px}
.brand .dot{width:46px;height:46px;border-radius:50%;background:var(--ink);flex:none}
.brand span{font-size:30px;line-height:1.15;font-weight:700;color:var(--ink)}

.headline{position:absolute;left:516px;top:96px;font-size:37px;line-height:42px;color:var(--ink);font-weight:400;letter-spacing:-.3px}
.headline em{font-style:normal;color:var(--blue)}
.mission{position:absolute;left:518px;top:254px;width:530px;font-size:15px;line-height:19.5px;color:var(--text)}
.mission strong{color:var(--ink)}
.theory{position:absolute;left:518px;top:356px;font-size:15px;color:var(--text)}
.theory b{color:var(--blue)}
.pie{position:absolute;left:518px;top:386px;list-style:none;font-size:17px;color:var(--ink)}
.pie li{position:absolute;display:flex;align-items:center;gap:10px;white-space:nowrap}
.pie i{font-style:normal;width:30px;height:30px;border-radius:50%;background:#1a1a1a;color:#fff;font-size:13px;font-weight:700;display:flex;align-items:center;justify-content:center}

.services{position:absolute;left:0;top:446px;width:1200px;height:411px;
  background:radial-gradient(ellipse at 55% 65%,var(--night-blue) 0%,#101820 45%,var(--night) 100%)}
.services h2{position:absolute;left:128px;top:24px;font-family:"Roboto Condensed",Arial,sans-serif;font-size:40px;font-weight:400;color:#fff;letter-spacing:.5px}
.btn{position:absolute;display:flex;align-items:center;justify-content:center;font-family:"Roboto Condensed",Arial,sans-serif;font-weight:700;color:#2a1f05;
  background:linear-gradient(#e9c874,#b88e33);border-radius:2px}
.btn.all{left:913px;top:36px;width:148px;height:29px;font-size:15px}
.btn.all::after{content:"";position:absolute;right:-12px;top:0;border-left:12px solid #cfa64c;border-top:14.5px solid transparent;border-bottom:14.5px solid transparent}
.card{position:absolute;top:84px;width:218px;height:270px}
.card .photo{width:218px;height:120px;border:2px solid var(--gold-dark);box-shadow:0 4px 10px rgba(0,0,0,.6)}
.card h3{margin-top:14px;font-size:18px;line-height:22px;font-weight:400;color:#fff}
.card p{margin-top:4px;font-size:12px;line-height:16px;color:var(--muted);text-align:justify}
.card p b{font-weight:400;color:var(--link)}
.card .btn{position:absolute;left:2px;top:238px;width:106px;height:30px;font-size:13.5px;clip-path:polygon(0 0,92% 0,100% 50%,92% 100%,0 100%)}

.footer{position:absolute;left:0;top:857px;width:1200px;height:180px;background:linear-gradient(#222,var(--footer))}
.col{position:absolute;top:28px;font-size:12.5px;line-height:17px;color:var(--footer-text)}
.col h4{font-family:"Roboto Condensed",Arial,sans-serif;font-size:14px;color:var(--gold);font-weight:700;margin-bottom:8px}
.col ul{list-style:none}
.social{display:flex;gap:18px;margin-top:10px}
.social li{display:flex;align-items:center;gap:6px;font-size:11.5px}
.social i{width:26px;height:26px;border-radius:3px;background:#6f6f6f}
.social li:first-child i{background:var(--gold-dark)}
.seal{position:absolute;left:926px;top:26px;width:120px;display:flex;flex-direction:column;align-items:center;gap:8px}
.seal .dot{width:84px;height:84px;border-radius:50%;border:3px solid #555}
.seal span{font-size:12px;color:#6a6a6a;font-weight:700;text-align:center}
</style>
</head>
<body>

<section class="intro">
  <header class="topbar">
    <div class="mark" role="img" aria-label="Lantern and Keystone"></div>
    <ul class="nav">
      <li class="current" style="left:90px">HOME</li>
      <li style="left:165px">WHO WE ARE</li>
      <li style="left:287px">SERVICES</li>
      <li style="left:393px">FAQ</li>
      <li style="left:458px">ENQUIRY</li>
      <li style="left:558px">CONTACT US</li>
    </ul>
    <div class="call">
      <svg width="24" height="24" viewBox="0 0 24 24" aria-hidden="true"><circle cx="12" cy="12" r="10.5" fill="none" stroke="#e6e6e6" stroke-width="1.6"/><path d="M8.5 6.5l2 2.4-1.2 1.5c.7 1.6 1.8 2.7 3.3 3.4l1.5-1.2 2.4 2-1.2 1.8c-3.6-.3-7.4-4.1-7.7-7.8z" fill="#e6e6e6"/></svg>
      <span>Call: <b>0400 318 274</b></span>
    </div>
  </header>

  <div class="brand">
    <div class="dot"></div>
    <span>Lantern and Keystone</span>
  </div>

  <h1 class="headline"><em>Lantern and Keystone</em> is a<br>South Australian owned business<br>and we service all of Australia</h1>

  <p class="mission">Through integrity and <strong>professionalism</strong> we will use our experience and resources as well as thinking outside the box to deliver results and services that exceed our clients' expectations. The team at Lantern and Keystone are welcoming, <strong>understanding</strong> and are more than happy to meet all your needs, wants and expectations.</p>
  <p class="theory">We employ the <b>P.I.E.</b> theory developed by our chief investigator.</p>
  <ul class="pie">
    <li style="left:0"><i>1</i>Professionalism</li>
    <li style="left:224px"><i>2</i>Integrity</li>
    <li style="left:388px"><i>3</i>Efficiency</li>
  </ul>
</section>

<section class="services">
  <h2>SERVICES</h2>
  <a class="btn all">VIEW ALL SERVICES</a>

  <article class="card" style="left:129px">
    <div class="photo" role="img" aria-label="Photo of crime scene tape reading unsolved over a case board" style="background:linear-gradient(135deg,#8a7a5a,#d8c34a 55%,#7a6a4a)"></div>
    <h3>Unsolved Cases</h3>
    <p>If you are <b>unsatisfied</b> with the investigation performed by other private investigation agencies and or law enforcement we will.</p>
    <a class="btn">Read More</a>
  </article>

  <article class="card" style="left:371px">
    <div class="photo" role="img" aria-label="Photo of a group of people in a scuffle" style="background:linear-gradient(135deg,#2f4f7a,#5d6f88 50%,#3a2c28)"></div>
    <h3>Bullying/Stalking</h3>
    <p>Is someone stalking you or bullying you? Well we will get the proof and evidence <b>whether</b> it be online and or in real life.</p>
    <a class="btn">Read More</a>
  </article>

  <article class="card" style="left:614px">
    <div class="photo" role="img" aria-label="Photo of an empty child's tricycle on a lawn" style="background:linear-gradient(135deg,#c9c2b4,#8d7f6c 60%,#6d6354)"></div>
    <h3>Child recovery</h3>
    <p>Our wide range of <b>resources</b>, skills and experience will help you find your children and get them back to you safe and sound.</p>
    <a class="btn">Read More</a>
  </article>

  <article class="card" style="left:856px">
    <div class="photo" role="img" aria-label="Photo of a dog behind cage bars" style="background:linear-gradient(135deg,#3a3a3a,#6a5a44 60%,#2a2622)"></div>
    <h3>Animal Cruelty</h3>
    <p>Animals have feelings too and they deserve to live a happy and safe life. We can help to make sure that happens. If you suspect a...</p>
    <a class="btn">Read More</a>
  </article>
</section>

<footer class="footer">
  <div class="col" style="left:139px">
    <h4>SITEMAP</h4>
    <ul><li>Home</li><li>About us</li><li>Faq's</li><li>Services</li><li>Contact Us</li></ul>
  </div>
  <div class="col" style="left:338px">
    <h4>CONTACT DETAILS</h4>
    <ul><li>Phone: 0400 318 274</li><li>managers@lanternandkeystone.example</li><li>Contact hours: 24 hours a day</li></ul>
  </div>
  <div class="col" style="left:605px">
    <h4>FOLLOW US</h4>
    <ul class="social">
      <li><i></i>Friendwall</li>
      <li><i></i>Chirper</li>
      <li><i></i>Linkwork</li>
    </ul>
  </div>
  <div class="seal">
    <div class="dot"></div>
    <span>Lantern and Keystone</span>
  </div>
</footer>

</body>
</html>
```